Solo Law Practice Website Design

I am starting a solo law practice that will specialize in criminal defense and family law.

I have a rudimentary understanding of Wordpress as used through the tidalnest web services. The winning design would be compatible with this system so that I can modify content on my own.

I have supplied the written content and the components that I am looking for at the domain name: morganvaleslaw.com.

I would like to take that content and work it into a website that looks more professional and inviting. The two most important goals of the website are ease of navigation and rich content for search engine spiders (for example, integrating articles into pages rather than linking to a word document).

The winning design should be turnkey for me to upload immediately.
Updates

Reason: I will be traveling.

Target Market(s)

Individuals looking for legal services.

Industry/Entity Type

Defense

Requirements
Must have
• My picture should appear at least once in the site.

The design should allow a space for me to post blog or legal updates. Additionally, there should be functionality for me to add additional articles to the site.
Nice to have
• Appropriate pictures for a legal website to break-up text on pages.

Simple flash features that won't significantly slow loading times.

Widgets that drive traffic to a contact page or function.

```html
<!DOCTYPE html>
<html lang="en">
<head>
<meta charset="utf-8">
<title>Law Offices of Morgan Vales PLLC</title>
<link href="https://fonts.googleapis.com/css2?family=Source+Sans+3:wght@400;600;700&family=Ubuntu:wght@500&display=swap" rel="stylesheet">
<style>
:root{
  --brown-dark:#33240f;
  --brown:#3d2b16;
  --cream:#efe9e1;
  --cream-light:#f8f5f1;
  --text:#3b3126;
  --muted:#6e6558;
  --link:#2d64b0;
  --white:#ffffff;
}
*{box-sizing:border-box;margin:0;padding:0}
html,body{width:801px;height:1200px;overflow:hidden}
body{font-family:"Source Sans 3",sans-serif;color:var(--text);background:#f4f1ed;position:relative}
.topbar{position:absolute;left:0;top:0;width:801px;height:30px;background:var(--brown-dark)}
.social{position:absolute;right:80px;top:9px;display:flex;gap:4px}
.social span{width:14px;height:14px;border-radius:2px;background:#4a78b8}
.header{position:absolute;left:0;top:30px;width:801px;height:365px;background:linear-gradient(180deg,var(--cream-light),var(--cream))}
.brand{position:absolute;left:80px;top:8px;display:flex;align-items:center;gap:7px}
.brand .mark{width:93px;height:93px;border-radius:50%;background:#6b4d25;border:3px solid #b08a50}
.brand .name{font-size:19px;line-height:19px;color:var(--brown);font-weight:400;letter-spacing:-.3px}
.address{position:absolute;right:80px;top:21px;text-align:right;font-size:8.8px;line-height:10.6px;color:var(--brown);text-transform:uppercase}
.address .gap{margin-top:3px}
.hero{position:absolute;left:72px;top:139px;width:650px;height:256px;background:var(--white);box-shadow:0 0 10px rgba(0,0,0,.25);overflow:hidden}
.hero .photo{position:absolute;left:280px;top:6px;width:370px;height:250px;background:radial-gradient(circle at 40% 45%,#e9c8a8 0,#c79a74 28%,#6b4628 60%,#3b2514 100%)}
.hero h2{position:absolute;left:37px;top:65px;font-size:12.5px;font-weight:700;color:var(--brown-dark)}
.hero p{position:absolute;left:37px;top:95px;width:200px;font-size:10.6px;line-height:18.6px;color:var(--brown-dark);text-transform:uppercase}
.btn{display:inline-block;background:var(--brown-dark);color:var(--white);font-weight:700;border-radius:2px;box-shadow:0 2px 3px rgba(0,0,0,.3);text-align:center}
.hero .btn{position:absolute;left:35px;top:183px;width:81px;height:21px;line-height:21px;font-size:8.5px}
.arrow{position:absolute;top:242px;width:28px;height:52px;background:var(--white);border-radius:26px;box-shadow:0 0 4px rgba(0,0,0,.3)}
.arrow.left{left:72px}.arrow.right{left:701px}
.arrow svg{position:absolute;top:16px;left:7px}
.nav{position:absolute;left:0;top:395px;width:801px;height:31px;background:linear-gradient(var(--brown),var(--brown-dark));display:flex;justify-content:center;align-items:center;gap:16px}
.nav a{color:var(--white);font-size:8.4px;text-decoration:none;text-transform:uppercase}
.main{position:absolute;left:73px;top:430px;width:447px}
.main h1{font-size:16.5px;font-weight:600;color:var(--brown)}
.lede{font-size:8.8px;margin-top:12px}
.about{display:flex;gap:5px;margin-top:10px}
.about .portrait{flex:0 0 159px;height:145px;background:linear-gradient(135deg,#4a2d18,#8a6a4a 50%,#2c1c10);border:1px solid #2b1d0f}
.copy{font-size:8.4px;line-height:16px;color:var(--muted)}
.copy b{color:var(--brown-dark);font-size:9px}
.attorney{font-size:12.5px;font-weight:700;color:var(--brown);margin-top:4px}
.areas-title{font-size:9px;font-weight:700;margin-top:16px;color:var(--brown-dark)}
.areas{display:flex;gap:16px;margin-top:15px}
.area{width:137px}
.area .pic{height:80px;border:2px solid #2b1d0f}
.area h3{font-size:11.6px;font-weight:600;color:var(--brown-dark);margin-top:8px;text-transform:uppercase}
.area p{font-size:7.2px;line-height:10.7px;margin-top:5px;text-align:justify;height:125px}
.area .btn{width:57px;height:15px;line-height:15px;font-size:7.2px}
.contact{position:absolute;left:73px;top:1053px;width:440px;font-size:8.4px;line-height:16px;color:var(--muted)}
.contact b{color:var(--brown-dark);font-size:9px}
.share{position:absolute;left:73px;top:1102px;font-size:8.8px;font-weight:700;color:var(--brown-dark)}
.share-row{position:absolute;left:73px;top:1122px;display:flex;gap:8px;align-items:center;font-size:8px}
.share-row .chip{height:12px;padding:0 5px;line-height:12px;border:1px solid #bbb;background:#eef1f6;color:#333;font-weight:600}
.share-row .chip.fb{background:#4a6aa5;color:#fff;border-color:#4a6aa5}
.share-row a{color:var(--link);text-decoration:none}
.sidebar-head{position:absolute;left:549px;top:431px;width:170px}
.sidebar-head h4{position:absolute;left:0;top:16px;font-family:"Ubuntu",sans-serif;font-weight:500;font-size:17px;color:var(--brown)}
.sidebar-head svg{position:absolute;left:137px;top:0}
.sidebar{position:absolute;left:541px;top:472px;width:187px;height:558px;background:var(--brown);padding:12px 8px;color:#e9e0d3}
.sidebar h5{font-family:"Ubuntu",sans-serif;font-weight:500;font-size:15px;color:var(--white);line-height:17px;text-transform:uppercase}
.sidebar label{display:block;font-size:8.8px;margin-top:7px}
.field{height:14px;background:var(--white);margin-top:3px;border:1px solid #ccc}
.select{width:110px;height:14px;background:var(--white);color:#222;font-size:8px;padding-left:2px;line-height:13px;margin-top:3px;position:relative}
.select:after{content:"";position:absolute;right:2px;top:2px;width:9px;height:9px;border:1px solid #888;background:#eee}
.area-box{width:145px;height:88px;background:var(--white);margin-top:5px}
.pill{display:inline-block;background:#f2f2f2;color:#222;font-size:8.4px;border-radius:8px;padding:1px 6px;margin-top:7px}
.rule{border-top:2px dotted #8b7555;margin:16px 0 14px;width:150px}
.hint{font-size:7.4px;color:#8c7c66;line-height:12px;margin-top:6px}
.email{height:14px;background:var(--white);color:#222;font-size:8px;line-height:13px;padding-left:3px;margin-top:5px}
.search{display:flex;gap:2px;margin-top:7px}
.search .q{width:154px;height:14px;background:var(--white);color:#222;font-size:7.6px;line-height:13px;padding-left:3px}
.search .go{width:15px;height:14px;background:var(--white);color:#222;font-size:6.5px;line-height:13px;text-align:center}
.footer{position:absolute;left:0;top:1155px;width:801px;height:45px;background:#d9d6d2}
.footer p{position:absolute;left:81px;top:13px;font-size:7.6px;color:var(--brown-dark)}
</style>
</head>
<body>
<div class="topbar"><div class="social"><span></span><span></span><span></span></div></div>

<header class="header">
  <div class="brand">
    <div class="mark" role="img" aria-label="Circular brand seal"></div>
    <div class="name">Law Offices of<br>Morgan Vales PLLC</div>
  </div>
  <div class="address">
    <p>Morgan Vales<br>Attorney-at-law</p>
    <p class="gap">PO Box 418203<br>St. Paul, MN 55127</p>
    <p class="gap">(612) 555-0148</p>
    <p class="gap">morgan@morganvaleslaw.com<br>www.morganvaleslaw.com</p>
  </div>
</header>

<section class="hero">
  <div class="photo" role="img" aria-label="Portrait photograph of the attorney smiling in a shirt and tie"></div>
  <h2>OUR PROMISE IS PEACE OF MIND</h2>
  <p>Take advantage of our extensive knowledge base, commitment to superior client service, and dedication to excellence.</p>
  <span class="btn">READ MORE</span>
</section>
<div class="arrow left"><svg width="14" height="20"><path d="M11 2 3 10l8 8" stroke="#33240f" stroke-width="3" fill="none"/></svg></div>
<div class="arrow right"><svg width="14" height="20"><path d="M3 2l8 8-8 8" stroke="#33240f" stroke-width="3" fill="none"/></svg></div>

<nav class="nav">
  <a>Home</a><a>Contact Me</a><a>Criminal Law</a><a>Family Law</a><a>Will Drafting</a><a>Attorney Profile</a><a>Fees</a><a>Legal Updates</a><a>Online Resources</a><a>Articles</a>
</nav>

<main class="main">
  <h1>Specializing in Criminal Defense and Family Law</h1>
  <p class="lede">Delivering legal services in the greater Twin Cities area.</p>
  <div class="about">
    <div class="portrait" role="img" aria-label="Portrait photograph of the attorney in front of law books"></div>
    <div class="copy">
      <p><b>About Me.</b> My practice is focused on accomplishing your goals through results-oriented work at a discount price. For your convenience, I handle legal matters throughout the Twin Cities, including Hennepin, Ramsey, Anoka, and Washington counties. I understand that legal issues can appear complicated, and that is why I take a hands-on approach to guiding you through your legal needs.</p>
      <p style="margin-top:2px"><b>Personal Attention.</b> I control the size of my practice so that I am able to devote 100% of my effort to each case. I have no “associates” so I handle every case personally.</p>
    </div>
  </div>
  <div class="attorney">MORGAN VALES, ATTORNEY</div>
  <div class="copy" style="margin-top:2px">
    <p><b>General Practice.</b> I am available to provide your defense if you are accused of a felony or misdemeanor. Additionally, I can work with you on family matters such as divorce, child custody, wills, and nuptial agreements.</p>
    <p><b>In our first consultation,</b> I will take time to listen to your individual situation. I will explain the legal issues, and the risks involved in each course of action we may pursue so that you can make informed decisions about how to proceed.</p>
  </div>
  <p class="areas-title">My areas of specialization are as follows:</p>
  <div class="areas">
    <div class="area">
      <div class="pic" role="img" aria-label="Photograph of handcuffed hands" style="background:linear-gradient(135deg,#5d5248,#b49a84 50%,#3b342e)"></div>
      <h3>Criminal Law</h3>
      <p>Convictions carry serious consequences and can often have a negative financial impact as well as putting your freedom in jeopardy. I know how to work on your behalf because I used to work at the Dakota Ridge County Attorney's Office and appeared on the prosecution's behalf for more than 600 cases. I will prepare your defense, negotiate plea bargains if desired, or take the case to trial.</p>
      <span class="btn">READ MORE</span>
    </div>
    <div class="area">
      <div class="pic" role="img" aria-label="Photograph of hands turning pages of a law book" style="background:linear-gradient(135deg,#2e2116,#8a6c4c 55%,#1d140c)"></div>
      <h3>Experience Matters</h3>
      <p>Every case is different. You can take comfort knowing that I have appeared in court on a wide variety of cases including assault, drug possession and distribution, DWI, disorderly conduct, theft, burglary, domestic assault, check forgery, violations or orders for protection, firearms violations and DWI test refusals. I am also prepared to handle your probation violation or expungement.</p>
      <span class="btn">READ MORE</span>
    </div>
    <div class="area">
      <div class="pic" role="img" aria-label="Photograph of a wooden gavel with a family label" style="background:radial-gradient(circle at 50% 60%,#b08a4a,#f3f1ee 60%)"></div>
      <h3>Family Law</h3>
      <p>I am prepared to handle your family law concerns. I can guide you through the process of child custody matters, divorce, wills and nuptial agreements to ensure that you receive a fair and equitable result on these sensitive matters.</p>
      <span class="btn">READ MORE</span>
    </div>
  </div>
</main>

<p class="contact"><b>Contact me.</b> To discuss how the Law Offices of Morgan Vales can help you, call us at (612) 555-0148 to arrange for you free consultation.</p>
<p class="share">Share this:</p>
<div class="share-row">
  <span class="chip fb">Share</span><span class="chip">Post</span><span class="chip">0</span>
  <a>✉ Email</a><a>⎙ Print</a>
</div>

<div class="sidebar-head">
  <h4>VOICE LINE</h4>
  <svg width="34" height="34" viewBox="0 0 34 34"><path d="M2 2h28v22H18l-6 6v-6H2z" fill="#33240f"/><path d="M10 8c1-1 3-1 3 1l-1 3c2 3 3 4 6 5l2-1c2 0 2 2 1 3-3 3-9-1-11-4s-2-6 0-7z" fill="#fff"/></svg>
</div>
<aside class="sidebar">
  <h5>Contact Form</h5>
  <label>Name(required)</label><div class="field"></div>
  <label>Email</label><div class="field"></div>
  <label>Phone</label><div class="field"></div>
  <label>Preferred Contact Method</label><div class="select">Phone</div>
  <label>Please briefly describe your legal issue (required)</label>
  <div class="area-box"></div>
  <span class="pill">Subscribe</span>
  <div class="rule"></div>
  <h5>Subscribe to receive legal updates</h5>
  <p class="hint">Enter your email address to receive notifications of legal updates by e-mail</p>
  <div class="email">Email Address</div>
  <span class="pill">Subscribe</span>
  <div class="rule"></div>
  <h5>Search</h5>
  <div class="search"><div class="q">SEARCH HERE...</div><div class="go">GO</div></div>
</aside>

<footer class="footer"><p>© 2012 Law Offices of Morgan Vales PLLC</p></footer>
</body>
</html>
```